Modern Catering Company needs Letterhead Design

We need a letterhead design that will make effective use of the corporate logo and color scheme, along with careful typography, helps this letterhead design communicate the brand well. We do have a corporate logo, however feel free to enhance the color scheme with gold and purple. We are serving a very upscale clientele so the letterhead has to reflect elegance, professionalism, cleanliness, and modern style. We are branding the company so the letterhead and business cards must fit the brand story. There should be no cartoonish elements in the design and we are looking for sharper lines.

Target Market(s)

Businesses and upscale clientele

Industry/Entity Type

Catering

Contact Information for Business Card

while this design can have any number of quirks and distinctions, it needs to be cohesive with the entire brand story clean, professional but edgy

Requirements
Must have
• must have good and carefully placement of it’s logo and where you place the text or the message. Colors blue, very deep purple, jewel tones not pastels, gold. Blue must be the primary color you may accent with purple or gold. Contact information is as follows: Co-Owners/ Chefs: R. Hollowell & T. Brenn, phone: 414-555-0182 email:Contact@emberoakcatering.example, address: 6172 W Larkmoor Ln, Milwaukee, WI 53299
Should not have
• pastel colors, Do not add the BBQ information to the letterhead or business card it was a mistake by the previous designer.

```html
<!DOCTYPE html>
<html lang="en">
<head>
<meta charset="utf-8">
<title>Ember Oak Catering — Stationery</title>
<link rel="stylesheet" href="https://fonts.googleapis.com/css2?family=Oswald:wght@300;400&family=Lato:ital,wght@0,300;0,400;0,700;1,400;1,700&display=swap">
<style>
  :root{
    --navy:#1b3a63;
    --gold:#f3c453;
    --sky:#a9c4e8;
    --paper:#ffffff;
    --stage:#3f3f3f;
    --ink-blue:#2d5aa8;
    --ink-grey:#777777;
  }
  *{margin:0;padding:0;box-sizing:border-box}
  html,body{width:1200px;height:800px;overflow:hidden;background:var(--stage)}
  .canvas{position:relative;width:1200px;height:800px}

  .wordmark{font-family:'Oswald',sans-serif;font-weight:400;color:var(--gold);text-align:center;line-height:1}
  .wordmark .name{display:block;letter-spacing:-0.5px}
  .wordmark .trade{display:block;letter-spacing:0.55em;margin-left:0.55em}

  /* Letterhead */
  .letterhead{position:absolute;left:92px;top:22px;width:480px;height:624px;background:var(--paper)}
  .letterhead .sidebar{position:absolute;left:0;top:0;width:162px;height:100%;background:var(--navy);border-right:4px solid var(--gold)}
  .sidebar .wordmark{position:absolute;left:0;width:162px;top:186px}
  .sidebar .wordmark .name{font-size:31px}
  .sidebar .wordmark .trade{font-size:14px;margin-top:5px}
  .rule{position:absolute;height:2px;background:var(--gold)}
  .sidebar .rule{left:32px;width:94px}
  .sidebar .rule.top{top:269px}
  .sidebar .rule.bottom{top:378px}
  .owners{position:absolute;left:16px;right:10px;top:296px;font-family:'Lato',sans-serif;color:var(--gold)}
  .owners .primary{font-size:16px;font-weight:700;letter-spacing:0.8px}
  .owners .secondary{font-size:20px;font-weight:300;color:var(--sky);letter-spacing:4px;line-height:1}
  .owners .role{font-size:13.5px;font-weight:700;letter-spacing:0.6px}
  .contact{position:absolute;left:16px;right:6px;top:404px;font-family:'Lato',sans-serif;color:var(--gold)}
  .contact .phone{font-size:18px;letter-spacing:1.5px}
  .contact .email{font-size:8px;font-style:italic;letter-spacing:0.4px;margin-top:2px}
  .contact .address{font-size:10.5px;font-style:italic;font-weight:700;letter-spacing:1px;line-height:1.6;margin-top:3px}

  /* Folder */
  .folder{position:absolute;left:600px;top:60px;width:509px;height:680px;background:var(--navy)}
  .folder .rule{left:146px;width:212px;height:3px}
  .folder .rule.top{top:26px}
  .folder .rule.bottom{top:655px}
  .folder .wordmark{position:absolute;left:0;width:100%;top:336px}
  .folder .wordmark .name{font-size:60px}
  .folder .wordmark .trade{font-size:27px;margin-top:8px}

  /* Business cards */
  .card{position:absolute;top:666px;width:198px;height:114px}
  .card.front{left:122px;background:var(--paper);border-bottom:3px solid var(--navy)}
  .card.front::after{content:"";position:absolute;left:0;right:0;bottom:0;height:2px;background:var(--gold)}
  .card.back{left:344px;background:var(--navy)}
  .card.front .wordmark{position:absolute;left:0;width:100%;top:28px;color:var(--navy)}
  .card.front .wordmark .name{font-size:12px}
  .card.front .wordmark .trade{font-size:5.5px;margin-top:2px}
  .card.front .divider{position:absolute;top:60px;height:1px;background:var(--ink-grey);width:36px}
  .card.front .divider.left{left:0}
  .card.front .divider.right{right:0}
  .card-owner{position:absolute;left:0;width:100%;top:55px;text-align:center;font-family:'Lato',sans-serif}
  .card-owner .names{font-size:7.5px;color:var(--ink-blue)}
  .card-owner .role{font-size:5px;color:var(--ink-grey);letter-spacing:0.3px}
  .card-details{position:absolute;left:0;width:100%;top:86px;display:flex;justify-content:center;font-family:'Lato',sans-serif;font-size:5px;color:var(--ink-grey);line-height:1.7}
  .card-details .col-left{text-align:right;padding-right:4px;border-right:1px solid var(--ink-grey)}
  .card-details .col-right{text-align:left;padding-left:4px}
  .card.back .wordmark{position:absolute;left:0;width:100%;top:54px}
  .card.back .wordmark .name{font-size:24px}
  .card.back .wordmark .trade{font-size:10px;margin-top:3px}
</style>
</head>
<body>
<main class="canvas">

  <section class="letterhead" aria-label="Letterhead">
    <aside class="sidebar">
      <div class="wordmark">
        <span class="name">EMBER OAK</span>
        <span class="trade">CATERING</span>
      </div>
      <div class="rule top"></div>
      <div class="owners">
        <p class="primary">R. Hollowell</p>
        <p class="secondary">T. Brenn</p>
        <p class="role">Co-Owners/Chefs</p>
      </div>
      <div class="rule bottom"></div>
      <address class="contact" style="font-style:normal">
        <p class="phone">414-555-0182</p>
        <p class="email">Contact@emberoakcatering.example</p>
        <p class="address">6172 W Larkmoor Ln<br>Milwaukee, WI 53299</p>
      </address>
    </aside>
  </section>

  <section class="folder" aria-label="Presentation folder">
    <div class="rule top"></div>
    <div class="wordmark">
      <span class="name">EMBER OAK</span>
      <span class="trade">CATERING</span>
    </div>
    <div class="rule bottom"></div>
  </section>

  <section class="card front" aria-label="Business card front">
    <div class="wordmark">
      <span class="name">EMBER OAK</span>
      <span class="trade">CATERING</span>
    </div>
    <div class="divider left"></div>
    <div class="divider right"></div>
    <div class="card-owner">
      <p class="names">R. Hollowell &amp; T. Brenn</p>
      <p class="role">Co-Owners / Chefs</p>
    </div>
    <div class="card-details">
      <div class="col-left">6172 W Larkmoor Ln<br>Milwaukee, WI 53299</div>
      <div class="col-right">414-555-0182<br>Contact@emberoakcatering.example</div>
    </div>
  </section>

  <section class="card back" aria-label="Business card back">
    <div class="wordmark">
      <span class="name">EMBER OAK</span>
      <span class="trade">CATERING</span>
    </div>
  </section>

</main>
</body>
</html>
```